Design a Business Card for a restaurant ( 2 sides)

I need design for restaurant.

In the files you will see the content ( see the [login to view URL]) of the first side and link to the website of the restaurant. Please don't use black. The colors we prefer are red and gold like in the file: logo.jpg. I want you also use the symbol of "Trong Dong" , more see. [login to view URL] , in the visit cards as relief coating ( see photo)

In the backside, i want to have 10 places to stamp on it, when customer eat by us. And small text in the bottom " Liegt die Rechung über 20 Euro erhalten Sie einen Stempel von uns. Wenn Sie 10 Stempel gesammelt haben, gibt es einen Gutschein im Wert von 20 Euro."

Upload your desing with Mockup will increase your chance to win.

Be CREATIVE . Thanks.

```html
<!DOCTYPE html>
<html lang="de">
<head>
<meta charset="utf-8">
<title>Sen Vang – Visitenkarte</title>
<link rel="stylesheet" href="https://fonts.googleapis.com/css2?family=Quicksand:wght@400;500;600&display=swap">
<style>
  :root {
    --page: #ecebe8;
    --maroon: #7a3340;
    --maroon-deep: #5a2030;
    --maroon-light: #8e4452;
    --gold: #d9a52c;
    --gold-light: #f4c95a;
    --gold-deep: #a87818;
    --cream: #f3e6d9;
    --ink-gold: #5a3a0c;
  }
  * { box-sizing: border-box; margin: 0; padding: 0; }
  html, body { width: 1200px; height: 749px; overflow: hidden; }
  body {
    background: var(--page);
    font-family: "Quicksand", sans-serif;
    position: relative;
  }
  .card {
    position: absolute;
    top: 200px;
    width: 540px;
    height: 350px;
    border-radius: 4px;
    overflow: hidden;
    background:
      repeating-linear-gradient(45deg, rgba(255,255,255,0.03) 0 2px, rgba(0,0,0,0.03) 2px 4px),
      radial-gradient(ellipse at 35% 30%, var(--maroon-light), var(--maroon) 55%, var(--maroon-deep));
    box-shadow: 0 10px 28px rgba(0,0,0,0.22);
    color: var(--cream);
  }
  .card--front { left: 40px; }
  .card--back { left: 620px; }

  /* front */
  .brand-badge {
    position: absolute; left: 26px; top: 18px;
    width: 168px; height: 66px; border-radius: 50%;
    background: var(--maroon-deep);
    box-shadow: 0 2px 6px rgba(0,0,0,0.35);
    display: flex; align-items: center; justify-content: center;
    z-index: 2;
  }
  .brand-name {
    font-weight: 600; font-size: 22px; color: var(--cream); white-space: nowrap;
  }
  .name-band {
    position: absolute; left: 170px; right: 0; top: 52px; height: 46px;
    background: linear-gradient(180deg, var(--gold-light), var(--gold) 55%, var(--gold-deep));
    display: flex; align-items: center; padding-left: 34px;
    overflow: hidden;
  }
  .name-band__text {
    font-size: 22px; font-weight: 500; color: var(--ink-gold);
    white-space: nowrap;
  }
  .contact {
    position: absolute; left: 30px; top: 118px;
    font-size: 15px; line-height: 30px; letter-spacing: 0.3px;
    white-space: nowrap;
  }
  .website {
    position: absolute; left: 30px; bottom: 28px;
    font-size: 18px; letter-spacing: 0.3px;
    white-space: nowrap;
  }
  .drum-emblem {
    position: absolute; right: 30px; bottom: 34px;
    width: 150px; height: 150px; border-radius: 50%;
    background: radial-gradient(circle, #d8c7a0 0%, #b59a62 45%, #7d6a45 80%, #4b3d28 100%);
    box-shadow: 0 0 0 6px rgba(60,20,25,0.6), 0 4px 10px rgba(0,0,0,0.4);
  }

  /* back */
  .back-brand {
    position: absolute; right: 28px; top: 22px;
    font-size: 16px; font-weight: 600; color: var(--cream);
  }
  .stamps {
    position: absolute; left: 40px; right: 40px; top: 78px;
    display: grid; grid-template-columns: repeat(5, 1fr); row-gap: 26px;
    justify-items: center;
  }
  .stamp {
    width: 74px; height: 74px; border-radius: 50%;
    background: radial-gradient(circle at 40% 35%, var(--gold-light), var(--gold) 55%, var(--gold-deep));
    box-shadow: 0 3px 6px rgba(0,0,0,0.35), inset 0 0 0 3px rgba(255,230,150,0.35);
  }
  .stamp-note {
    position: absolute; left: 30px; right: 30px; bottom: 22px;
    font-size: 12.5px; line-height: 18px; text-align: center; color: var(--cream);
  }
</style>
</head>
<body>
  <section class="card card--front" aria-label="Vorderseite">
    <div class="brand-badge"><span class="brand-name">Sen Vang</span></div>
    <div class="name-band"><span class="name-band__text">Sen Vang Vietnam Restaurant</span></div>
    <div class="contact">
      <p>Adresse: Lindenweg 12, 30159 Hannover</p>
      <p>Tel.: +49 511 2468 1350</p>
    </div>
    <p class="website">Website: www.senvang-hannover.de</p>
    <div class="drum-emblem" role="img" aria-label="Bronze drum emblem in relief"></div>
  </section>

  <section class="card card--back" aria-label="Rückseite">
    <p class="back-brand">Sen Vang</p>
    <div class="stamps">
      <span class="stamp"></span><span class="stamp"></span><span class="stamp"></span><span class="stamp"></span><span class="stamp"></span>
      <span class="stamp"></span><span class="stamp"></span><span class="stamp"></span><span class="stamp"></span><span class="stamp"></span>
    </div>
    <p class="stamp-note">Liegt die Rechnung über 20 Euro, erhalten Sie einen Stempel von uns. Wenn Sie 10 Stempel gesammelt haben, gibt es einen Gutschein im Wert von 20 Euro.</p>
  </section>
</body>
</html>
```